Tavelin: A Friday night of the Kindled Word Flyer

We are holding 2 Friday night events, one on 10/25/19 and the other on 11/29/19.
The time frame is 6:30pm-9:00pm. These services will be a time of prayer/healing for the sick and will be prophetic as well. (There will be prophets prophesying over people)

The event is called: Tavelin: A Friday night of the Kindled Word
The flyer should also include the phrase/excerpt: "And they prophesied also".

Keywords/Phrases: Prophetic, Healing, Climbing in the Spirit, Higher level of Anointing...

Target Market(s)

those looking for healing, seeking a word from God

Colors

Designer to choose colors to be used in the design.

Requirements
Must have
• The event is called: Tavelin: A Friday night of the Kindled Word
• The flyer should also include the phrase/excerpt: "And they prophesied also".
• It must include the Quorvel logo attached, either is fine, we have attached two different versions.
• It must have the dates, location, time
• Dates: October 25, 2019 and November 29, 2019
• Location: Loftmere Community Center
• (Downtown Portland) 248 Wendlow Street
• Portland, ME 04102
• Time: 6:30pm-9:00pm
• Contact Info: Tel. 207-583-2914
• email: contact@ambervale.example
• web: www.quorvel.example
Nice to have
• creativity in color scheme, the meaning of the word Tavelin conveyed in a classy artistic way/design.
Should not have
• Crosses, pictures of churches

```html
<!DOCTYPE html>
<html lang="en">
<head>
<meta charset="utf-8">
<title>Tavelin: A Friday night of the Kindled Word</title>
<link rel="stylesheet" href="https://fonts.googleapis.com/css2?family=Cinzel:wght@400;500&family=Montserrat:wght@300;400;800&family=Roboto:wght@400&display=swap">
<style>
  :root {
    --page-bg: #d6d6d6;
    --flyer-black: #0c0c0c;
    --flyer-charcoal: #2a2a2a;
    --amber: #f7941d;
    --amber-deep: #d9780f;
    --divider-tone: #b8660d;
    --ring-bronze: #5a3a10;
    --ink: #111111;
    --white: #ffffff;
    --time-grey: #d9d9d9;
  }
  html, body {
    margin: 0;
    padding: 0;
    width: 703px;
    height: 1200px;
    overflow: hidden;
    background: var(--page-bg);
  }
  .canvas {
    width: 703px;
    height: 1200px;
    display: flex;
    align-items: center;
    justify-content: center;
  }
  .flyer {
    display: block;
    width: 703px;
    height: 993px;
  }
  .brand-name { font-family: "Cinzel", serif; font-size: 50px; font-weight: 400; fill: var(--white); letter-spacing: 1px; }
  .event-title { font-family: "Cinzel", serif; font-size: 70px; font-weight: 400; fill: var(--ink); }
  .event-subtitle { font-family: "Montserrat", sans-serif; font-size: 21px; font-weight: 300; fill: var(--ink); letter-spacing: 0.5px; }
  .event-quote { font-family: "Cinzel", serif; font-size: 16.5px; fill: var(--ink); letter-spacing: 0.5px; }
  .feature-label { font-family: "Montserrat", sans-serif; font-size: 14px; font-weight: 800; fill: var(--white); letter-spacing: 0.3px; }
  .date-line { font-family: "Montserrat", sans-serif; font-size: 25px; font-weight: 800; fill: var(--ink); letter-spacing: 0.5px; }
  .time-line { font-family: "Montserrat", sans-serif; font-size: 24px; font-weight: 800; fill: var(--ink); letter-spacing: 0.5px; }
  .venue-line { font-family: "Roboto", sans-serif; font-size: 16.5px; fill: var(--white); }
  .call-line { font-family: "Montserrat", sans-serif; font-size: 16px; font-weight: 400; fill: var(--ink); letter-spacing: 0.5px; }
  .contact-line { font-family: "Roboto", sans-serif; font-size: 12px; fill: var(--ink); }
</style>
</head>
<body>
<main class="canvas">
  <svg class="flyer" viewBox="0 0 662 935" xmlns="http://www.w3.org/2000/svg">
    <defs>
      <radialGradient id="flyerGlow" cx="50%" cy="40%" r="70%">
        <stop offset="0" stop-color="var(--flyer-charcoal)"/>
        <stop offset="1" stop-color="var(--flyer-black)"/>
      </radialGradient>
      <radialGradient id="sunsetGlow" cx="50%" cy="35%" r="70%">
        <stop offset="0" stop-color="#f9a233"/>
        <stop offset="0.7" stop-color="var(--amber)"/>
        <stop offset="1" stop-color="var(--amber-deep)"/>
      </radialGradient>
    </defs>

    <rect class="flyer-backdrop" width="662" height="935" fill="url(#flyerGlow)" role="img" aria-label="Dark silhouette of a worshipper with raised arms against a black sky"/>

    <g class="brand">
      <circle cx="196" cy="104" r="8" fill="var(--amber)"/>
      <text class="brand-name" x="345" y="122" text-anchor="middle">QUORVEL</text>
    </g>

    <g class="medallion">
      <circle cx="333" cy="357" r="202" fill="var(--ring-bronze)"/>
      <circle cx="333" cy="357" r="193" fill="url(#sunsetGlow)" role="img" aria-label="Orange sunset with a faint figure lifting its arms"/>
      <text class="event-title" x="333" y="347" text-anchor="middle">TAVELIN</text>
      <text class="event-subtitle" x="333" y="395" text-anchor="middle">A FRIDAY NIGHT OF THE</text>
      <text class="event-subtitle" x="333" y="423" text-anchor="middle">KINDLED WORD</text>
      <rect class="quote-divider" x="268" y="444" width="127" height="6" fill="var(--divider-tone)" role="img" aria-label="Ornamental divider above the quote"/>
      <text class="event-quote" x="333" y="472" text-anchor="middle">“AND THEY PROPHESIED ALSO”</text>
      <rect class="quote-divider" x="268" y="481" width="127" height="6" fill="var(--divider-tone)" role="img" aria-label="Ornamental divider below the quote"/>
    </g>

    <g class="features">
      <g class="feature" transform="translate(128 0)">
        <circle cx="0" cy="597" r="10" fill="none" stroke="var(--white)" stroke-width="2"/>
        <path d="M-5 596l5 5 9-12" fill="none" stroke="var(--amber)" stroke-width="3"/>
        <text class="feature-label" x="0" y="632" text-anchor="middle">PROPHETIC</text>
      </g>
      <g class="feature" transform="translate(250 0)">
        <circle cx="0" cy="597" r="10" fill="none" stroke="var(--white)" stroke-width="2"/>
        <path d="M-5 596l5 5 9-12" fill="none" stroke="var(--amber)" stroke-width="3"/>
        <text class="feature-label" x="0" y="632" text-anchor="middle">HEALING</text>
      </g>
      <g class="feature" transform="translate(372 0)">
        <circle cx="0" cy="597" r="10" fill="none" stroke="var(--white)" stroke-width="2"/>
        <path d="M-5 596l5 5 9-12" fill="none" stroke="var(--amber)" stroke-width="3"/>
        <text class="feature-label" x="0" y="632" text-anchor="middle">CLIMBING IN</text>
        <text class="feature-label" x="0" y="650" text-anchor="middle">THE SPIRIT</text>
      </g>
      <g class="feature" transform="translate(520 0)">
        <circle cx="0" cy="597" r="10" fill="none" stroke="var(--white)" stroke-width="2"/>
        <path d="M-5 596l5 5 9-12" fill="none" stroke="var(--amber)" stroke-width="3"/>
        <text class="feature-label" x="0" y="632" text-anchor="middle">HIGHER LEVEL</text>
        <text class="feature-label" x="0" y="650" text-anchor="middle">OF ANOINTING</text>
      </g>
    </g>

    <g class="schedule">
      <rect x="59" y="678" width="544" height="32" fill="var(--amber)"/>
      <text class="date-line" x="331" y="704" text-anchor="middle">OCTOBER 25 &amp; NOVEMBER 29, 2019</text>
      <rect x="218" y="719" width="228" height="32" fill="var(--time-grey)"/>
      <text class="time-line" x="332" y="744" text-anchor="middle">6:30PM-9:00PM</text>
    </g>

    <g class="venue">
      <text class="venue-line" x="331" y="792" text-anchor="middle">Loftmere Community Center, (Downtown Portland) 248 Wendlow</text>
      <text class="venue-line" x="331" y="813" text-anchor="middle">Street Portland, ME 04102</text>
    </g>

    <g class="contact">
      <path d="M0 922H662V935H0z" fill="var(--amber)"/>
      <path d="M138 922c18 0 22-6 28-22 8-22 20-28 40-28h250c20 0 32 6 40 28 6 16 10 22 28 22z" fill="var(--amber)"/>
      <text class="call-line" x="331" y="896" text-anchor="middle">CALL US NOW&#160;&#160;207-583-2914</text>
      <g class="mail-icon" fill="none" stroke="var(--ink)" stroke-width="1">
        <rect x="184" y="909" width="12" height="8"/>
        <path d="M184 909l6 5 6-5"/>
      </g>
      <text class="contact-line" x="200" y="917">contact@ambervale.example</text>
      <g class="web-icon" fill="none" stroke="var(--ink)" stroke-width="1">
        <circle cx="370" cy="913" r="5.5"/>
        <path d="M364.5 913h11M370 907.5v11"/>
      </g>
      <text class="contact-line" x="380" y="917">www.quorvel.example</text>
    </g>
  </svg>
</main>
</body>
</html>
```